Business Cards for an engineering & contracting company
Korvane Group
Business Cards for an engineering & contracting company - Architecture
Creative Brief
Professional
Architect Marwan Tarek Korvane
CEO - Project Manager
Chiyah, Blvd Rue Doumani, Next to Meridel Plaza, Korvane Tower, Blk B - 2nd floor
marwan@korvanegroup-example.com
www.korvanegroup-example.com
the word "Architect" can be written in a nice design before the name, The name is "Marwan Tarek Korvane". The company name is "Korvane Group" The country is " Beirut, Lebanon" Its preferable is the card is made of 2 or 3 colors that make it impressive
A design that is related to the company description, which is (architecture, engineering, design, contracting and construction) The logo may be a solution if its alone or with something else added to it.
Korvane Korvane
I'd like to see other stationery designs too in addition to the business card.

```html
<!DOCTYPE html>
<html lang="en">
<head>
<meta charset="utf-8">
<title>Korvane Group — Stationery</title>
<link rel="stylesheet" href="https://fonts.googleapis.com/css2?family=Open+Sans:wght@400;600&display=swap">
<style>
  :root{
    --bg:#eceef0;
    --paper:#ffffff;
    --blue:#1f6fe6;
    --navy:#2a5a9e;
    --grey:#9aa0a6;
    --ink:#4a4f55;
    --light-ink:#8a8f95;
  }
  *{box-sizing:border-box;margin:0;padding:0}
  html,body{width:1200px;height:936px;overflow:hidden;background:var(--bg)}
  body{position:relative;font-family:"Open Sans",Arial,sans-serif;color:var(--ink)}
  .sheet{position:absolute;background:var(--paper);overflow:hidden}
  .band{position:absolute;top:0;right:0;height:100%}
  .brand{text-align:center;line-height:1}
  .brand-name{font-family:"Open Sans",Arial,sans-serif;font-weight:600;color:var(--navy);letter-spacing:.02em;white-space:nowrap}
  .brand-tag{font-family:"Open Sans",Arial,sans-serif;font-weight:400;color:var(--grey);letter-spacing:.14em;text-transform:uppercase;white-space:nowrap}

  /* Letterhead */
  .letterhead{left:183px;top:61px;width:388px;height:548px}
  .letterhead .brand{position:absolute;left:22px;top:34px;width:120px}
  .letterhead .brand-name{font-size:12px}
  .letterhead .brand-tag{font-size:4.2px;margin-top:4px}
  .letter-body{position:absolute;left:22px;top:136px;width:290px;font-size:5.4px;line-height:1.65;color:var(--light-ink)}
  .letter-body p{margin-bottom:8px}
  .signature{display:block;width:36px;height:12px;background:linear-gradient(90deg,#cfd3d8,#e6e8eb);border-radius:2px;margin:3px 0 5px}
  .sender strong{display:block;color:var(--ink);font-weight:600}
  .letter-contact{position:absolute;left:22px;top:386px;font-size:5px;line-height:1.8;color:var(--light-ink)}
  .letter-contact div{display:flex;align-items:center;gap:4px}
  .dot{width:5px;height:5px;border-radius:50%;background:var(--blue);display:inline-block}

  /* Folder */
  .folder{left:635px;top:38px;width:419px;height:571px}
  .folder .brand{position:absolute;left:78px;width:330px;top:318px}
  .folder .brand{left:28px;width:330px}
  .folder .brand-name{font-size:25px}
  .folder .brand-tag{font-size:7.5px;margin-top:7px}

  /* Business cards */
  .card-front{left:43px;top:655px;width:240px;height:99px}
  .card-front .brand{position:absolute;left:6px;top:40px;width:100px}
  .card-front .brand-name{font-size:8.5px}
  .card-front .brand-tag{font-size:3px;margin-top:3px}
  .card-panel{position:absolute;right:0;top:0;width:130px;height:100%;background:var(--blue);color:#fff;padding:12px 8px 0 12px;font-size:4.6px;line-height:1.7;white-space:nowrap}
  .card-panel strong{display:block;font-size:6px;font-weight:600}
  .card-panel .title{margin-bottom:5px;opacity:.9}
  .card-back{left:43px;top:782px;width:240px;height:100px}
  .card-back .brand{position:absolute;left:0;width:240px;top:40px}
  .card-back .brand-name{font-size:10px}
  .card-back .brand-tag{font-size:3.4px;margin-top:3px}

  /* Envelope front */
  .envelope{left:305px;top:673px;width:390px;height:203px}
  .envelope .brand{position:absolute;left:20px;top:26px;width:110px}
  .envelope .brand-name{font-size:10px}
  .envelope .brand-tag{font-size:3.4px;margin-top:3px}
  .envelope-address{position:absolute;left:20px;top:52px;width:240px;font-size:4px;line-height:1.5;color:var(--light-ink)}

  /* Envelope back */
  .envelope-back{left:737px;top:673px;width:421px;height:203px}
  .flap{position:absolute;left:0;top:0;width:100%;height:110px}
  .flap-url{position:absolute;left:0;top:32px;width:100%;text-align:center;color:#fff;font-size:7.5px;letter-spacing:.18em}
</style>
</head>
<body>

<section class="sheet letterhead">
  <div class="brand">
    <div class="brand-name">Korvane Group</div>
    <div class="brand-tag">Engineering &amp; Contracting</div>
  </div>
  <div class="letter-body">
    <p>June 5, 2024<br>Korvane Group, Harvel, Beirut</p>
    <p>Dear Client,</p>
    <p>Thank you for choosing our team for your next project. We design, engineer and build homes and offices with care, precision and a clear plan from the first sketch to the final handover. Every stage is guided by our engineers.</p>
    <p>Our site teams keep you informed with weekly reports, budgets and timelines so that nothing is left to chance.</p>
    <p>We look forward to working with you and turning your vision into a lasting structure that feels like home for years to come.</p>
    <p class="sender">Best regards,
      <span class="signature" role="img" aria-label="Handwritten signature"></span>
      <strong>Marwan Tarek Korvane</strong>CEO - Project Manager
    </p>
  </div>
  <div class="letter-contact">
    <div><span class="dot"></span>+961 1 555 0142</div>
    <div><span class="dot"></span>marwan@korvanegroup-example.com</div>
    <div><span class="dot"></span>www.korvanegroup-example.com</div>
    <div><span class="dot"></span>Harvel, Blvd Rue Doumani, Next to Meridel Plaza</div>
  </div>
  <svg class="band" width="60" height="548" viewBox="0 0 60 548" preserveAspectRatio="none" aria-hidden="true">
    <path d="M34 0 Q4 274 34 548" fill="none" stroke="var(--grey)" stroke-width="2"/>
    <path d="M60 0 L40 0 Q12 274 40 548 L60 548 Z" fill="var(--blue)"/>
  </svg>
</section>

<section class="sheet folder">
  <div class="brand">
    <div class="brand-name">Korvane Group</div>
    <div class="brand-tag">Engineering &amp; Contracting</div>
  </div>
  <svg class="band" width="90" height="571" viewBox="0 0 90 571" preserveAspectRatio="none" aria-hidden="true">
    <path d="M52 0 Q8 286 52 571" fill="none" stroke="var(--grey)" stroke-width="3"/>
    <path d="M90 0 L62 0 Q20 286 62 571 L90 571 Z" fill="var(--blue)"/>
  </svg>
</section>

<section class="sheet card-front">
  <div class="brand">
    <div class="brand-name">Korvane Group</div>
    <div class="brand-tag">Engineering &amp; Contracting</div>
  </div>
  <div class="card-panel">
    <strong>Marwan Tarek Korvane</strong>
    <div class="title">CEO - Project Manager</div>
    <div>+961 1 555 0142</div>
    <div>marwan@korvanegroup-example.com</div>
    <div>www.korvanegroup-example.com</div>
    <div>Harvel, Korvane Tower, Blk B</div>
  </div>
</section>

<section class="sheet card-back">
  <div class="brand">
    <div class="brand-name">Korvane Group</div>
    <div class="brand-tag">Engineering &amp; Contracting</div>
  </div>
</section>

<section class="sheet envelope">
  <div class="brand">
    <div class="brand-name">Korvane Group</div>
    <div class="brand-tag">Engineering &amp; Contracting</div>
  </div>
  <div class="envelope-address">Harvel, Blvd Rue Doumani, Next to Meridel Plaza, Korvane Tower, Blk B - 2nd floor</div>
  <svg class="band" width="56" height="203" viewBox="0 0 56 203" preserveAspectRatio="none" aria-hidden="true">
    <path d="M28 0 Q12 101 28 203" fill="none" stroke="var(--grey)" stroke-width="2"/>
    <path d="M56 0 L36 0 Q20 101 36 203 L56 203 Z" fill="var(--blue)"/>
  </svg>
</section>

<section class="sheet envelope-back">
  <svg class="flap" viewBox="0 0 421 110" preserveAspectRatio="none" aria-hidden="true">
    <path d="M0 0 H421 V40 Q421 92 366 96 L55 96 Q0 92 0 40 Z" fill="var(--blue)"/>
    <path d="M55 101 L366 101 Q416 98 418 62" fill="none" stroke="var(--grey)" stroke-width="1.5"/>
  </svg>
  <div class="flap-url">www.korvanegroup-example.com</div>
</section>

</body>
</html>
```